Website for Nonprofit for kids whose parents have been wounded

We need a web design for a nonprofit that serves children who have been severely burned as well as those whose parents have been wounded during military service. We will be based out of hospitals and will need a format that will encourage trust, safety, and respect. We are stick with a lot of red white and blue. We will also be looking to have a space for donations.

Target Market(s)

Kids and parents of military veterans

Industry/Entity Type

Non Profit

Number of Pages Required

5+ page

Font styles to use
Serif
Decorative

Colors
ec1f27
ffffff
0255a3

Requirements
Must have
• Be both appealing to children and adults. Create a reputable face for our organization. We need an area for donations.
Nice to have
• Something unique

```html
<!DOCTYPE html>
<html lang="en">
<head>
<meta charset="utf-8">
<title>Harborlight Kids Project Inc.</title>
<link href="https://fonts.googleapis.com/css2?family=Roboto:wght@400;500;700&family=Roboto+Condensed:wght@400;700&display=swap" rel="stylesheet">
<style>
:root{
  --red:#d3343b;
  --red-bright:#ec1f27;
  --blue:#1e9bd7;
  --navy:#0255a3;
  --ink:#333333;
  --muted:#777777;
  --light:#f2f2f2;
  --line:#dddddd;
  --dark:#2b2b2b;
  --darker:#1f1f1f;
  --white:#ffffff;
}
*{box-sizing:border-box;margin:0;padding:0}
html,body{width:1200px;height:2868px;overflow:hidden}
body{font-family:"Roboto",Arial,sans-serif;color:var(--ink);background:var(--white);font-size:13px;line-height:1.5}
.wrap{width:980px;margin:0 auto;position:relative}
.btn{display:inline-block;font-family:"Roboto Condensed",Arial,sans-serif;font-weight:700;text-transform:uppercase;color:var(--white);border:none;letter-spacing:.3px}
.btn-red{background:var(--red)}
.btn-blue{background:var(--blue)}

/* header */
.site-header{height:112px;position:relative;background:var(--white);border-bottom:1px solid var(--line)}
.brand{position:absolute;left:20px;top:40px;display:flex;align-items:center;gap:10px}
.brand-dot{width:26px;height:26px;border-radius:50%;background:var(--red)}
.brand-name{font-family:"Roboto Condensed",Arial,sans-serif;font-weight:700;font-size:20px;color:var(--navy)}
.main-nav{position:absolute;left:455px;top:62px;display:flex;gap:28px;font-size:15px;color:var(--ink)}
.phone{position:absolute;right:28px;top:10px;display:flex;align-items:center;gap:8px;font-size:20px;color:var(--ink)}
.phone-icon{width:26px;height:26px;border-radius:50%;background:var(--red);display:flex;align-items:center;justify-content:center}
.header-donate{position:absolute;right:28px;top:56px;padding:10px 26px;font-size:15px;border-radius:3px}

/* hero */
.hero{height:448px;position:relative;background:linear-gradient(90deg,#c9c3bb 0%,#9c8f84 45%,#5a4c44 75%,#3b302b 100%)}
.hero-photo{position:absolute;inset:0}
.hero-text{position:absolute;right:90px;top:88px;width:400px;text-align:right;font-family:"Roboto Condensed",Arial,sans-serif;font-weight:700;font-size:29px;line-height:1.32;color:var(--white)}
.hero-donate{position:absolute;right:90px;top:318px;padding:16px 34px;font-size:22px}
.hero-arrow{position:absolute;top:206px;width:34px;height:38px;background:rgba(0,0,0,.45);display:flex;align-items:center;justify-content:center}
.hero-arrow.left{left:0}.hero-arrow.right{right:0}

/* ways to help */
.ways{height:352px;background:var(--red);position:relative}
.ways-row{display:flex;justify-content:space-between;width:900px;margin:0 auto;padding-top:40px}
.way{width:180px;text-align:center;color:var(--white)}
.way-badge{width:116px;height:116px;margin:0 auto;border-radius:50%;border:2px solid rgba(255,255,255,.55);display:flex;align-items:center;justify-content:center}
.way-badge span{width:70px;height:70px;border-radius:50%;background:rgba(255,255,255,.18);display:flex;align-items:center;justify-content:center}
.way h3{font-family:"Roboto Condensed",Arial,sans-serif;font-size:17px;margin:16px 0 8px;letter-spacing:.5px}
.way p{font-size:12px;line-height:1.45;opacity:.95}
.way .more{display:inline-block;margin-top:14px;font-size:13px;font-weight:700}

/* about */
.about{height:288px;background:var(--light)}
.about .wrap{display:flex;gap:40px;padding-top:22px}
.about-main{width:680px}
.about-side{width:260px}
.section-head{font-family:"Roboto Condensed",Arial,sans-serif;font-weight:700;font-size:22px;color:var(--ink);padding-bottom:8px;border-bottom:2px solid var(--line);position:relative;margin-bottom:14px}
.section-head::after{content:"";position:absolute;left:0;bottom:-2px;width:70px;height:2px;background:var(--red)}
.about-main p{font-size:12px;color:var(--muted);line-height:1.6}
.about-main h4{font-size:14px;color:var(--red);margin:14px 0 4px}
.inquiry input{display:block;width:100%;height:30px;border:1px solid var(--line);background:var(--white);margin-bottom:10px;padding:0 10px;font-size:12px;color:var(--muted);font-family:inherit}
.inquiry .btn{padding:7px 22px;font-size:13px}

/* programs */
.programs{height:460px;padding-top:52px}
.center-head{text-align:center;font-family:"Roboto Condensed",Arial,sans-serif;font-weight:700;font-size:30px;color:var(--ink)}
.center-rule{width:980px;margin:12px auto 0;height:2px;background:var(--line);position:relative}
.center-rule::after{content:"";position:absolute;left:440px;width:100px;height:2px;background:var(--red)}
.program-row{display:flex;gap:12px;width:980px;margin:32px auto 0}
.program{width:186px;height:272px;position:relative}
.program.featured{background:linear-gradient(160deg,#3aa7de,#1a73b8);color:var(--white);padding:80px 16px 0}
.program.featured h3{font-family:"Roboto Condensed",Arial,sans-serif;font-size:20px}
.program.featured p{font-size:11px;margin:6px 0 12px}
.program.featured .btn{padding:6px 16px;font-size:12px}
.p2{background:linear-gradient(160deg,#c8a58a,#8a6a58)}
.p3{background:linear-gradient(160deg,#9fb7c4,#4f6f55)}
.p4{background:linear-gradient(160deg,#a3b09a,#3e4e44)}
.p5{background:linear-gradient(160deg,#8c97a6,#3d4552)}

/* donate band */
.donate-band{height:280px;position:relative;background:linear-gradient(180deg,#1d3c66 0%,#1a2e4f 60%,#4b4238 100%);text-align:center;color:var(--white)}
.donate-band h2{padding-top:56px;font-family:"Roboto Condensed",Arial,sans-serif;font-size:42px;letter-spacing:1px}
.donate-band p{font-family:"Roboto Condensed",Arial,sans-serif;font-weight:700;font-size:19px;margin-top:6px}
.donate-band .btn{margin-top:20px;padding:12px 28px;font-size:17px}

/* testimonials */
.testimonials{height:380px;padding-top:44px}
.testimonials .center-head{font-size:32px}
.sub{text-align:center;font-size:12px;color:var(--muted);margin-top:4px}
.quotes{display:flex;justify-content:space-between;width:920px;margin:36px auto 0}
.quote{width:440px;display:flex;gap:22px}
.quote-person{width:120px;text-align:center}
.avatar{width:110px;height:110px;border-radius:50%;margin:0 auto;background:linear-gradient(160deg,#b9a395,#5e6f7d)}
.quote-person span{display:block;font-size:13px;color:var(--red);margin-top:8px}
.quote-text{position:relative;font-size:12px;color:var(--muted);line-height:1.6;padding:10px 22px}
.quote-text::before{content:"\201C";position:absolute;left:0;top:-8px;font-size:42px;color:#999;font-family:Georgia,serif}
.quote-text::after{content:"\201D";position:absolute;right:0;bottom:-26px;font-size:42px;color:#999;font-family:Georgia,serif}
.slider-nav{display:flex;justify-content:center;gap:6px;margin-top:34px}
.slider-nav span{width:22px;height:22px;border:1px solid var(--line);display:flex;align-items:center;justify-content:center}

/* cta strip */
.cta-strip{height:100px;background:var(--red)}
.cta-strip .wrap{display:flex;align-items:center;justify-content:space-between;height:100px}
.cta-strip p{font-family:"Roboto Condensed",Arial,sans-serif;font-weight:700;font-size:22px;color:var(--white);width:700px;line-height:1.3}
.cta-strip .btn{padding:14px 30px;font-size:22px}

/* footer */
.footer-nav{height:80px;background:var(--dark);display:flex;justify-content:center;align-items:center;gap:34px;font-size:14px;color:var(--white);border-bottom:1px solid #3c3c3c;position:relative}
.footer-nav .mark{position:absolute;left:580px;bottom:-14px;width:40px;height:28px;background:var(--dark);display:flex;justify-content:center}
.footer-cols{height:320px;background:var(--dark);color:#cccccc}
.footer-cols .wrap{display:flex;gap:70px;padding-top:40px}
.footer-cols h4{font-size:14px;color:var(--white);padding-bottom:10px;border-bottom:1px solid #444;margin-bottom:16px;text-transform:uppercase}
.col-contact{width:240px;font-size:13px;line-height:1.7}
.col-contact strong{color:var(--red)}
.col-contact .row{display:flex;gap:8px;align-items:center;margin-top:6px}
.col-map{width:300px}
.map{height:200px;background:linear-gradient(150deg,#e9e6df,#d6d3cb);position:relative}
.col-news{width:300px;font-size:13px}
.col-news input{display:block;width:100%;height:38px;border:none;margin:16px 0 10px;padding:0 12px;font-family:inherit;font-size:13px}
.col-news .btn{padding:10px 22px;font-size:16px}
.footer-bottom{height:48px;background:var(--darker)}
.footer-bottom .wrap{display:flex;justify-content:space-between;align-items:center;height:48px;font-size:12px;color:#aaa}
.footer-bottom .btn{padding:9px 24px;font-size:18px;margin-right:160px}
</style>
</head>
<body>

<header class="site-header">
  <div class="brand"><span class="brand-dot"></span><span class="brand-name">Harborlight Kids Project Inc.</span></div>
  <nav class="main-nav"><span>About Us</span><span>Projects</span><span>Stories</span><span>Donate</span><span>Contact Us</span></nav>
  <div class="phone">
    <span class="phone-icon"><svg width="14" height="14" viewBox="0 0 24 24"><path fill="#fff" d="M6.6 10.8a15 15 0 0 0 6.6 6.6l2.2-2.2c.3-.3.7-.4 1-.2 1.1.4 2.3.6 3.6.6.6 0 1 .4 1 1V20c0 .6-.4 1-1 1A17 17 0 0 1 3 4c0-.6.4-1 1-1h3.5c.6 0 1 .4 1 1 0 1.3.2 2.5.6 3.6.1.3 0 .7-.2 1z"/></svg></span>
    (555) 014 2090
  </div>
  <span class="btn btn-red header-donate">Donate Now</span>
</header>

<section class="hero">
  <div class="hero-photo" role="img" aria-label="Photo of a smiling mother in a warm home interior"></div>
  <p class="hero-text">Help Make Sure That After Defending Our Freedom, Our Veterans And Their Loved Ones Get The Care They Earned</p>
  <span class="btn btn-blue hero-donate">Donate Now</span>
  <span class="hero-arrow left"><svg width="10" height="14" viewBox="0 0 10 14"><path d="M8 1 2 7l6 6" stroke="#fff" stroke-width="2" fill="none"/></svg></span>
  <span class="hero-arrow right"><svg width="10" height="14" viewBox="0 0 10 14"><path d="m2 1 6 6-6 6" stroke="#fff" stroke-width="2" fill="none"/></svg></span>
</section>

<section class="ways">
  <div class="ways-row">
    <div class="way">
      <div class="way-badge"><span><svg width="30" height="30" viewBox="0 0 24 24"><rect x="4" y="3" width="14" height="18" rx="1" fill="none" stroke="#fff" stroke-width="2"/><path d="M7 8h8M7 12h8M7 16h5" stroke="#fff" stroke-width="2"/></svg></span></div>
      <h3>ENROLL</h3>
      <p>Register your family with our hospital team and begin care today.</p>
      <span class="more">Read More</span>
    </div>
    <div class="way">
      <div class="way-badge"><span><svg width="30" height="30" viewBox="0 0 24 24"><circle cx="12" cy="8" r="4" fill="#fff"/><path d="M4 21c0-4.4 3.6-7 8-7s8 2.6 8 7z" fill="#fff"/></svg></span></div>
      <h3>VOLUNTEER</h3>
      <p>Give your time to support children and families during recovery.</p>
      <span class="more">Read More</span>
    </div>
    <div class="way">
      <div class="way-badge"><span><svg width="30" height="30" viewBox="0 0 24 24"><path d="M12 21 4 13a5 5 0 0 1 8-6 5 5 0 0 1 8 6z" fill="#fff"/></svg></span></div>
      <h3>SUPPORT</h3>
      <p>Fund care, comfort kits and programs for kids in our hospitals.</p>
      <span class="more">Read More</span>
    </div>
    <div class="way">
      <div class="way-badge"><span><svg width="30" height="30" viewBox="0 0 24 24"><circle cx="18" cy="5" r="3" fill="#fff"/><circle cx="6" cy="12" r="3" fill="#fff"/><circle cx="18" cy="19" r="3" fill="#fff"/><path d="m8.5 10.5 7-4M8.5 13.5l7 4" stroke="#fff" stroke-width="2"/></svg></span></div>
      <h3>SHARE</h3>
      <p>Spread our story so more military families can find help.</p>
      <span class="more">Read More</span>
    </div>
  </div>
</section>

<section class="about">
  <div class="wrap">
    <div class="about-main">
      <h2 class="section-head">What We Do</h2>
      <p>We work inside hospitals to care for children who have been severely burned and for kids whose parents were wounded in military service. Our team offers play therapy, counseling, tutoring and family support so that every child feels safe, respected and heard. We partner with doctors, nurses and veteran groups to bring comfort to each bedside and to help families stay close during long recoveries and new beginnings at home.</p>
      <h4>Our Mission</h4>
      <p>To give every child of a wounded service member the care, hope and joy they deserve, and to stand beside their families from the first hospital day until they are strong again.</p>
    </div>
    <div class="about-side">
      <h2 class="section-head">Quick Inquiry</h2>
      <form class="inquiry">
        <input type="text" placeholder="Name">
        <input type="text" placeholder="Email">
        <input type="text" placeholder="Your detail message">
        <span class="btn btn-blue">Submit</span>
      </form>
    </div>
  </div>
</section>

<section class="programs">
  <h2 class="center-head">Our Latest Programs</h2>
  <div class="center-rule"></div>
  <div class="program-row">
    <div class="program featured">
      <h3>A SMILE PROGRAM</h3>
      <p>Play days and gifts that bring joy to kids in care.</p>
      <span class="btn btn-red">Read More</span>
    </div>
    <div class="program p2" role="img" aria-label="Photo of a family gathered together"></div>
    <div class="program p3" role="img" aria-label="Photo of a veteran father with his child outdoors"></div>
    <div class="program p4" role="img" aria-label="Photo of a service member in uniform"></div>
    <div class="program p5" role="img" aria-label="Photo of a veteran in a wheelchair with a helper"></div>
  </div>
</section>

<section class="donate-band" role="img" aria-label="Background photo of soldiers beneath a flag">
  <h2>DONATE</h2>
  <p>Make a donation to support our veterans</p>
  <span class="btn btn-red">Donate Now</span>
</section>

<section class="testimonials">
  <h2 class="center-head">Words form Our Happy Veterans</h2>
  <p class="sub">See What Say About us</p>
  <div class="quotes">
    <div class="quote">
      <div class="quote-person"><div class="avatar" role="img" aria-label="Portrait photo of a veteran"></div><span>Lorem Ipsum</span></div>
      <p class="quote-text">The team cared for my son while I healed. He laughed again in the hospital, and our whole family felt safe, welcome and never alone.</p>
    </div>
    <div class="quote">
      <div class="quote-person"><div class="avatar" role="img" aria-label="Portrait photo of a veteran in uniform"></div><span>Lorem Ipsum</span></div>
      <p class="quote-text">After my injury my daughter was scared. Their staff gave her friends, games and hope, and helped us find our way back home together.</p>
    </div>
  </div>
  <div class="slider-nav">
    <span><svg width="8" height="10" viewBox="0 0 8 10"><path d="M6 1 2 5l4 4" stroke="#888" stroke-width="1.5" fill="none"/></svg></span>
    <span><svg width="8" height="10" viewBox="0 0 8 10"><path d="m2 1 4 4-4 4" stroke="#888" stroke-width="1.5" fill="none"/></svg></span>
  </div>
</section>

<section class="cta-strip">
  <div class="wrap">
    <p>Lorem ipsum dolor sit amet consectetur adipisicing elitsed do eiusmod tempor incididunt ut labore dolore magna aliqua.</p>
    <span class="btn btn-blue">Donate Now</span>
  </div>
</section>

<footer>
  <nav class="footer-nav">
    <span>Home</span><span>About Us</span><span>Projects</span><span>Stories</span><span>Donate</span><span>Contact Us</span>
    <span class="mark"><svg width="18" height="18" viewBox="0 0 18 18"><rect x="4" y="4" width="10" height="10" transform="rotate(45 9 9)" fill="none" stroke="#888" stroke-width="1.5"/></svg></span>
  </nav>
  <div class="footer-cols">
    <div class="wrap">
      <div class="col-contact">
        <h4>Contact Details</h4>
        <strong>Harborlight Kids Project Inc.</strong><br>
        Street Name City Name<br>State Zipcode
        <div class="row"><svg width="12" height="12" viewBox="0 0 24 24"><path fill="#ccc" d="M6.6 10.8a15 15 0 0 0 6.6 6.6l2.2-2.2c.3-.3.7-.4 1-.2 1.1.4 2.3.6 3.6.6.6 0 1 .4 1 1V20c0 .6-.4 1-1 1A17 17 0 0 1 3 4c0-.6.4-1 1-1h3.5c.6 0 1 .4 1 1 0 1.3.2 2.5.6 3.6.1.3 0 .7-.2 1z"/></svg>555 014 2090</div>
        <div class="row"><svg width="12" height="12" viewBox="0 0 24 24"><path fill="#ccc" d="M6.6 10.8a15 15 0 0 0 6.6 6.6l2.2-2.2c.3-.3.7-.4 1-.2 1.1.4 2.3.6 3.6.6.6 0 1 .4 1 1V20c0 .6-.4 1-1 1A17 17 0 0 1 3 4c0-.6.4-1 1-1h3.5c.6 0 1 .4 1 1 0 1.3.2 2.5.6 3.6.1.3 0 .7-.2 1z"/></svg>555 014 2091</div>
        <div class="row"><svg width="12" height="12" viewBox="0 0 24 24"><rect x="2" y="5" width="20" height="14" fill="none" stroke="#ccc" stroke-width="2"/><path d="m2 5 10 8 10-8" stroke="#ccc" stroke-width="2" fill="none"/></svg>hello@harborlightkids.org</div>
      </div>
      <div class="col-map">
        <h4>Location Map</h4>
        <div class="map" role="img" aria-label="Street map showing the office location">
          <svg style="position:absolute;left:136px;top:70px" width="28" height="40" viewBox="0 0 24 34"><path d="M12 0C5.4 0 0 5.2 0 11.8 0 20 12 34 12 34s12-14 12-22.2C24 5.2 18.6 0 12 0z" fill="#d3343b"/><circle cx="12" cy="12" r="4.5" fill="#fff"/></svg>
        </div>
      </div>
      <div class="col-news">
        <h4>Newsletter Signup</h4>
        <p>Get monthly stories and news about the children and families we serve.</p>
        <input type="text" placeholder="Enter your email">
        <span class="btn btn-blue">Submit</span>
      </div>
    </div>
  </div>
  <div class="footer-bottom">
    <div class="wrap">
      <span>Copyright © 2015 Harborlight. All rights reserved.</span>
      <span class="btn btn-blue">Donate Now</span>
    </div>
  </div>
</footer>

</body>
</html>
```